Professional & Modern Website Design for Ridgeline Site Fittings

Our company, a leader in custom furniture and joinery solutions for mining camps, needs a website overhaul. Our current site is looking dated and underwhelming, and we’re seeking a design that truly reflects our professionalism and expertise.

To Whom Are We Speaking?
Our target audience includes asset managers, procurement professionals, and senior-level management from international mining companies. We need a website that speaks directly to these key decision-makers, showcasing our value and expertise.

What We’re Looking For:
Fresh & Modern Aesthetic: We want our website to captivate visitors with a contemporary and sleek design.
Professional Appeal: The new design should convey our commitment to high-quality craftsmanship and service.
Visual Impact: Showcase our custom furniture and joinery work with stunning visuals that highlight our capabilities.
Brochure Alignment: The design should mirror the style and aesthetics of our attached brochure to ensure brand consistency and visual harmony.
Logo & Branding: We want to keep our current logo and branding. The red color should be retained but used sparingly as an accent color to complement the overall design.
Brand Book Usage: Attached is our Brand Book for our Hotel and Accommodation Company. Please use only the correct colors and text from this Brand Book for our Ridgeline Site Fittings Brand to ensure consistency and coherence across our branding.
Structured Layout: We require a total of 8 pages, including:
Landing Page: Featuring a prominent contact button
About
Services: Interior Design, Manufacturing, Delivery & Installation
Products: Furniture Packages, Joinery, Upholstery, Beds & Bedding

Our Goals:
Elevate Our Brand: Create a site that mirrors our reputation and industry leadership.
Enhance User Experience: Ensure a seamless, engaging experience for visitors.
Showcase Our Work: Promote our projects and services with impact.

Must include:
Contact us button
Geographical Reach

Previous company website: www.ridgelinesitefittings.com.au (we wish to convert some of the content from this website to the new platform). Competitor websites that we like: www.tablorvex.com.au,

For functionality we would like it to be designed on Wix.

```html
<!DOCTYPE html>
<html lang="en">
<head>
<meta charset="utf-8">
<title>Ridgeline Site Fittings</title>
<link href="https://fonts.googleapis.com/css2?family=Poppins:wght@300;400;500;600;700;800&display=swap" rel="stylesheet">
<style>
:root{
  --red:#e31e30;
  --ink:#1d1d1f;
  --grey:#6b6b6b;
  --light:#f4f4f4;
  --line:#cfcfcf;
  --dark:#2b2a2b;
  --white:#ffffff;
}
*{margin:0;padding:0;box-sizing:border-box}
html,body{width:1200px;height:4914px;overflow:hidden}
body{font-family:'Poppins',sans-serif;color:var(--ink);background:var(--white);position:relative}
.abs{position:absolute}
.btn{position:absolute;display:flex;align-items:center;justify-content:center;background:var(--red);color:var(--white);font-size:14px;font-weight:500;letter-spacing:.3px;text-transform:uppercase}
.btn.ghost{background:transparent;border:2px solid var(--white)}
.photo{position:absolute}

/* hero */
.hero-photo{left:0;top:0;width:1200px;height:770px;background:linear-gradient(135deg,#5a4a3a 0%,#8c7a66 35%,#3c3f45 65%,#a9a39a 100%)}
.hero-shade{left:0;top:0;width:1200px;height:770px;background:rgba(0,0,0,.28)}
.header{left:72px;top:50px;width:1082px;height:97px;background:var(--white);clip-path:polygon(0 0,100% 0,97% 100%,0 100%)}
.brand{position:absolute;display:flex;align-items:center;gap:10px}
.brand-mark{width:34px;height:34px;background:var(--red)}
.brand-name{font-weight:700;color:var(--ink);line-height:1.05}
.nav a{position:absolute;top:91px;font-size:14px;font-weight:500;color:var(--ink);text-decoration:none}
.welcome{left:475px;top:315px;width:269px;height:40px;background:var(--red);color:var(--white);font-size:26px;font-weight:500;display:flex;align-items:center;justify-content:center}
.hero-title{left:0;width:1200px;top:382px;text-align:center;color:var(--white);font-size:70px;font-weight:800;line-height:76px}

/* service cards */
.card{position:absolute;top:614px;height:355px;background:var(--white);box-shadow:0 10px 30px rgba(0,0,0,.12);clip-path:polygon(0 8%,100% 0,100% 100%,0 100%);text-align:center}
.card.red{background:var(--red);color:var(--white);clip-path:polygon(0 4%,100% 0,100% 100%,0 100%)}
.card .icon{position:absolute;left:50%;top:86px;width:86px;height:86px;margin-left:-43px;background:#fbe3e5}
.card.red .icon{background:rgba(255,255,255,.25)}
.card h3{position:absolute;top:186px;width:100%;font-size:20px;font-weight:500}
.card p{position:absolute;top:225px;left:20px;right:20px;font-size:12.5px;line-height:16px;color:var(--grey)}
.card.red p{color:var(--white)}
.card .btn{top:298px;width:158px;height:36px}

/* experience */
.exp-box{left:122px;top:1135px;width:115px;height:157px;border:14px solid var(--line);border-right-color:transparent}
.exp-num{left:168px;top:1150px;font-size:92px;font-weight:600;color:var(--red);line-height:120px}
.exp-label{left:292px;top:1196px;font-size:25px;font-weight:400}
.exp-text{left:122px;top:1326px;width:470px;font-size:12.5px;line-height:21px;color:var(--grey)}
.exp-photo{left:652px;top:1065px;width:447px;height:480px;background:linear-gradient(180deg,#4f6b85 0%,#7891a6 40%,#dcdcdc 70%,#8f8f8f 100%);clip-path:polygon(0 7%,100% 0,100% 100%,0 100%)}

/* split panels */
.band-photo{left:0;width:1200px}
.panel{position:absolute;background:rgba(255,255,255,.88)}
.eyebrow{font-size:14px;color:var(--red);text-transform:uppercase}
.panel h2{font-size:27px;font-weight:700;line-height:33px;text-transform:uppercase}
.panel p{font-size:12.5px;line-height:21px;color:var(--grey)}

/* products */
.section-title{left:0;width:1200px;text-align:center;font-size:27px;font-weight:700}
.rule{height:5px;background:var(--red)}
.prod-icon{position:absolute;width:70px;height:70px;background:#fbe3e5}
.prod-name{position:absolute;font-size:17px;font-weight:600;line-height:21px}

/* carousel */
.carousel{left:0;top:3160px;width:1200px;height:462px;background:linear-gradient(180deg,#d42a3a,#e5515e)}
.carousel h2{position:absolute;top:78px;width:100%;text-align:center;color:var(--white);font-size:26px;font-weight:700}
.slide{position:absolute;top:173px;width:237px;height:202px}
.arrow{position:absolute;top:260px;width:50px;height:50px;border-radius:50%;background:var(--white);display:flex;align-items:center;justify-content:center}

/* footer */
.footer{left:0;top:4556px;width:1200px;height:358px;background:var(--dark)}
.footer-brand{left:0;top:4556px;width:328px;height:358px;background:var(--white)}
.footer-title{position:absolute;color:var(--white);font-size:20px;font-weight:500}
.flink{position:absolute;left:430px;color:var(--white);font-size:14px;display:flex;align-items:center;gap:10px}
.flink svg{width:16px;height:10px}
.contact{position:absolute;left:652px;color:var(--white);font-size:12px;display:flex;align-items:center;gap:12px}
</style>
</head>
<body>

<!-- hero -->
<div class="photo hero-photo" role="img" aria-label="Modern camp bedroom with desk, shelving and upholstered bed"></div>
<div class="abs hero-shade"></div>
<div class="abs header"></div>
<div class="brand" style="left:112px;top:66px">
  <div class="brand-mark"></div>
  <div>
    <div class="brand-name" style="font-size:24px">RIDGELINE</div>
    <div class="brand-name" style="font-size:12px;font-weight:500">SITE FITTINGS</div>
    <div style="font-size:7px;color:var(--red);font-weight:600;margin-top:2px">The Future of Site Fittings is Here</div>
  </div>
</div>
<nav class="nav">
  <a style="left:400px">HOME</a>
  <a style="left:504px">ABOUT</a>
  <a style="left:616px">SERVICES</a>
  <a style="left:746px">PRODUCTS</a>
</nav>
<div class="btn" style="left:942px;top:82px;width:130px;height:38px;font-size:16px">Contact</div>
<div class="abs welcome">WELCOME TO</div>
<h1 class="abs hero-title">RIDGELINE SITE<br>FITTINGS</h1>

<div class="card" style="left:126px;width:303px">
  <div class="icon" role="img" aria-label="Design icon"></div>
  <h3>DESIGN</h3>
  <p>Our ongoing services are designed to keep your unit operating at peak efficiency without disruptive breakdowns.</p>
  <div class="btn" style="left:72px">Our Services</div>
</div>
<div class="card red" style="left:464px;width:303px">
  <div class="icon" role="img" aria-label="Manufacturing icon"></div>
  <h3>MANUFACTURING</h3>
  <p>Our ongoing services are designed to keep your unit operating at peak efficiency without disruptive breakdowns.</p>
  <div class="btn ghost" style="left:68px">Our Process</div>
</div>
<div class="card" style="left:801px;width:306px">
  <div class="icon" role="img" aria-label="Installation icon"></div>
  <h3>INSTALLATION</h3>
  <p>Our ongoing services are designed to keep your unit operating at peak efficiency without disruptive breakdowns.</p>
  <div class="btn" style="left:75px">Read More</div>
</div>

<!-- experience -->
<div class="abs exp-box"></div>
<div class="abs exp-num">25</div>
<div class="abs exp-label">Years of Experience</div>
<p class="abs exp-text">As a natural extension of our success in the hotel industry, Ridgeline Site Fittings was born. We recognized the need for high-quality, durable, and aesthetically pleasing furniture solutions in mining camp environments. Combining our expertise in hospitality with innovative design principles, we now bring the same level of excellence to mining camps across the globe.</p>
<div class="btn" style="left:122px;top:1460px;width:126px;height:30px;font-size:12px">Read More</div>
<div class="photo exp-photo" role="img" aria-label="Twin bed room with blue feature wall"></div>

<!-- concept -->
<div class="photo band-photo" style="top:1635px;height:479px;background:linear-gradient(90deg,#cfc8c0 0%,#b8aa98 45%,#7a5a3e 70%,#e8e6e2 100%)" role="img" aria-label="Furnished room with timber wardrobe and desk"></div>
<div class="panel" style="left:118px;top:1715px;width:572px;height:342px;clip-path:polygon(0 0,100% 0,86% 100%,0 100%)">
  <div class="eyebrow" style="position:absolute;left:64px;top:44px">We have you covered from</div>
  <h2 style="position:absolute;left:64px;top:80px">Concept to<br>Completion</h2>
  <p style="position:absolute;left:64px;top:168px;width:400px">Whether you require interior design expertise, assistance with tender submissions, custom joinery solutions, or furniture and room prototypes, we have the expertise and resources to deliver exceptional results.</p>
  <div class="btn" style="left:68px;top:272px;width:140px;height:32px;font-size:12px">Read More</div>
</div>

<!-- durable -->
<div class="photo band-photo" style="top:2118px;height:477px;background:linear-gradient(90deg,#5d6b80 0%,#8895a6 30%,#c8bfb2 60%,#eae6e0 100%)" role="img" aria-label="Upholstered bedhead with wall switches and a potted plant"></div>
<div class="panel" style="left:572px;top:2200px;width:576px;height:341px;clip-path:polygon(0 0,100% 0,100% 100%,14% 100%)">
  <h2 style="position:absolute;right:72px;top:52px;text-align:right">Durable, Functional<br>and Compliant</h2>
  <p style="position:absolute;right:72px;top:150px;width:340px;text-align:right;font-size:11px;line-height:15px">We understand the unique demands of mining operations and the need for durable, functional, and compliant furniture solutions. With our comprehensive packages, we aim to create comfortable and efficient living spaces for your mining workforce.</p>
  <div class="btn" style="left:358px;top:232px;width:144px;height:32px;font-size:12px">Read More</div>
</div>

<!-- products -->
<h2 class="abs section-title" style="top:2688px">OUR PRODUCTS</h2>
<div class="abs rule" style="left:528px;top:2730px;width:76px"></div>

<div class="prod-icon" style="left:38px;top:2814px" role="img" aria-label="Loose furniture icon"></div>
<div class="prod-name" style="left:134px;top:2828px">Loose Furniture<br>and case goods</div>
<div class="prod-icon" style="left:319px;top:2814px" role="img" aria-label="Artwork and lamps icon"></div>
<div class="prod-name" style="left:422px;top:2828px">Artwork, Lamps,<br>Artificial Plants</div>
<div class="prod-icon" style="left:607px;top:2814px" role="img" aria-label="Joinery icon"></div>
<div class="prod-name" style="left:712px;top:2828px">High Volume<br>Joinery</div>
<div class="prod-icon" style="left:893px;top:2814px" role="img" aria-label="Kitchen and dining icon"></div>
<div class="prod-name" style="left:998px;top:2832px">Kitchen and<br>Dining Furnitures</div>

<div class="prod-icon" style="left:38px;top:2960px" role="img" aria-label="Beds icon"></div>
<div class="prod-name" style="left:134px;top:2976px">Beds and<br>Beddings</div>
<div class="prod-icon" style="left:319px;top:2960px" role="img" aria-label="Window furnishing icon"></div>
<div class="prod-name" style="left:422px;top:2976px">Windows<br>Furnishing</div>
<div class="prod-icon" style="left:607px;top:2956px" role="img" aria-label="Outdoor furniture icon"></div>
<div class="prod-name" style="left:712px;top:2970px">Outdoor<br>Furniture</div>
<div class="prod-icon" style="left:893px;top:2956px" role="img" aria-label="Cleaning packs icon"></div>
<div class="prod-name" style="left:998px;top:2970px">Electrical and<br>Cleaning Packs</div>

<!-- carousel -->
<div class="abs carousel">
  <h2>THE FUTURE OF SITE FITTINGS IS HERE.</h2>
  <div class="slide" style="left:84px;background:linear-gradient(135deg,#f0ede8,#b9a48a)" role="img" aria-label="Bed with timber bedside"></div>
  <div class="slide" style="left:353px;background:linear-gradient(135deg,#c9ab85,#6b5a48)" role="img" aria-label="Bed with timber shelving"></div>
  <div class="slide" style="left:622px;background:linear-gradient(135deg,#e8e8e8,#3a3a3a)" role="img" aria-label="Black leather armchair"></div>
  <div class="slide" style="left:889px;background:linear-gradient(135deg,#ececec,#a87a4e)" role="img" aria-label="Timber bedside table"></div>
  <div class="arrow" style="left:9px"><svg width="16" height="20" viewBox="0 0 16 20"><path d="M12 2 4 10l8 8" fill="none" stroke="var(--red)" stroke-width="2.5"/></svg></div>
  <div class="arrow" style="left:1143px"><svg width="16" height="20" viewBox="0 0 16 20"><path d="M4 2l8 8-8 8" fill="none" stroke="var(--red)" stroke-width="2.5"/></svg></div>
</div>

<!-- geographical reach -->
<div class="photo" style="left:0;top:3625px;width:1200px;height:473px;background:linear-gradient(90deg,#e2e2e2 0%,#d6d6d6 50%,#c9b68e 75%,#d9d9d9 100%)" role="img" aria-label="World map highlighting Asia and Australia"></div>
<div class="panel" style="left:95px;top:3702px;width:573px;height:339px;background:var(--light);clip-path:polygon(0 0,100% 0,81% 100%,0 100%)">
  <h2 style="position:absolute;left:72px;top:100px">Geographical<br>Reach</h2>
  <div class="rule" style="position:absolute;left:72px;top:170px;width:66px;height:4px"></div>
  <p style="position:absolute;left:72px;top:190px;width:370px;font-size:10.5px;line-height:15px">With a global presence, our services extend to Australia, New Zealand, South East Asia, and the United Arab Emirates.</p>
</div>

<!-- partner -->
<div class="photo" style="left:0;top:4102px;width:1200px;height:450px;background:linear-gradient(135deg,#4a3a30 0%,#a0643a 35%,#3e4a52 65%,#b07a4a 100%)" role="img" aria-label="Aerial view of a mining landscape"></div>
<div class="panel" style="left:588px;top:4165px;width:572px;height:343px;background:rgba(255,255,255,.93);clip-path:polygon(0 0,100% 0,100% 100%,18% 100%)">
  <h2 style="position:absolute;right:72px;top:92px;text-align:right;font-weight:600;font-size:26px">Ridgeline Site Fittings<br>is your ultimate furniture<br>solutions partner.</h2>
  <div class="rule" style="position:absolute;right:76px;top:212px;width:76px;height:4px"></div>
  <div class="btn" style="left:356px;top:236px;width:142px;height:32px;font-size:12px">Read More</div>
</div>

<!-- footer -->
<div class="abs footer"></div>
<div class="abs footer-brand"></div>
<div class="brand" style="left:44px;top:4708px">
  <div class="brand-mark" style="width:44px;height:44px"></div>
  <div>
    <div class="brand-name" style="font-size:30px">RIDGELINE</div>
    <div class="brand-name" style="font-size:14px;font-weight:500">SITE FITTINGS</div>
  </div>
</div>
<h4 class="footer-title" style="left:418px;top:4630px">QUICK LINKS</h4>
<h4 class="footer-title" style="left:652px;top:4630px">CONTACT US</h4>
<h4 class="footer-title" style="left:946px;top:4634px">GET UPDATES</h4>

<div class="flink" style="top:4700px"><svg viewBox="0 0 16 10"><path d="M0 5h13M9 1l4 4-4 4" stroke="var(--red)" stroke-width="2" fill="none"/></svg>Home</div>
<div class="flink" style="top:4730px"><svg viewBox="0 0 16 10"><path d="M0 5h13M9 1l4 4-4 4" stroke="var(--red)" stroke-width="2" fill="none"/></svg>About</div>
<div class="flink" style="top:4760px"><svg viewBox="0 0 16 10"><path d="M0 5h13M9 1l4 4-4 4" stroke="var(--red)" stroke-width="2" fill="none"/></svg>Services</div>
<div class="flink" style="top:4790px"><svg viewBox="0 0 16 10"><path d="M0 5h13M9 1l4 4-4 4" stroke="var(--red)" stroke-width="2" fill="none"/></svg>Products</div>
<div class="flink" style="top:4820px"><svg viewBox="0 0 16 10"><path d="M0 5h13M9 1l4 4-4 4" stroke="var(--red)" stroke-width="2" fill="none"/></svg>Contact</div>

<div class="contact" style="top:4700px;color:var(--red)">Warren Hale MDIA</div>
<div class="contact" style="top:4740px"><svg width="16" height="16" viewBox="0 0 16 16"><path d="M3 1l3 3-2 2c1 2 3 4 5 5l2-2 3 3-2 3C7 15 1 9 1 3z" fill="var(--red)"/></svg>+61 (4) 555 0142</div>
<div class="contact" style="top:4780px"><svg width="16" height="14" viewBox="0 0 16 14"><rect x="1" y="2" width="14" height="10" fill="none" stroke="var(--red)" stroke-width="2"/><path d="M1 2l7 6 7-6" fill="none" stroke="var(--red)" stroke-width="2"/></svg>warren@ridgelinesitefittings.com.au</div>
<div class="contact" style="top:4818px"><svg width="16" height="14" viewBox="0 0 16 14"><rect x="1" y="2" width="14" height="10" fill="none" stroke="var(--red)" stroke-width="2"/><path d="M1 2l7 6 7-6" fill="none" stroke="var(--red)" stroke-width="2"/></svg>info@ridgelinesitefittings.com.au</div>

<div class="abs" style="left:952px;top:4699px;width:174px;height:29px;background:#fff;font-size:12px;color:#999;padding:6px 10px">Email Address</div>
<div class="btn" style="left:952px;top:4749px;width:174px;height:27px;font-size:12px;font-weight:600">Subscribe Now</div>

</body>
</html>
```